Healthcare Technology Company Business Card Design

Hi,

We require a new business card design thats catchy and professional.
Our target audience is healthcare professionals. See supplied artwork for our logo.

If you think its achievable please try add the tag line, not necessary however.
"Developing technologies to improve patient care and release operation benefits"

We'll require the following information on the card. No need to have the subject titles but i've referenced them for your convenience.

Personal Details
Paul Dwyer
Position: Director
Phone Number - 03 9472 5836
Mobile Number - 0438 275 904
Email: firstname.lastname@mediqbay.com.au

Company Details
Suite 31, 286 Keldon Street
Port Melbourne, Victoria
Fax: 03 8241 3975
mediqbay.com.au

Prefer a thinner design than the normal stock standard business card dimensions.
Please ensure there is adequate bleed.

Target Market(s)

Healthcare Professionals

Industry/Entity Type

Healthcare

Font styles to use
Sans Serif

Requirements
Must have
• Clean, Sharp Looks
Should not have
• Any healthcare symbols

```html
<!DOCTYPE html>
<html lang="en">
<head>
<meta charset="utf-8">
<title>MediqBay Business Card</title>
<link rel="stylesheet" href="https://fonts.googleapis.com/css2?family=Source+Sans+3:wght@400;600&display=swap">
<style>
  :root {
    --backdrop: #e4e2e0;
    --card-dark: #3d3d3d;
    --card-light: #ffffff;
    --navy: #234f66;
    --blue: #336a93;
    --orange: #f0922b;
    --ink: #3a3a3a;
  }
  * { box-sizing: border-box; margin: 0; padding: 0; }
  html, body {
    width: 1200px; height: 675px; overflow: hidden;
    background: var(--backdrop);
    font-family: "Source Sans 3", sans-serif;
  }
  .canvas {
    position: relative; width: 1200px; height: 675px;
    display: flex; align-items: center; justify-content: center; gap: 60px;
  }
  .card {
    position: relative; width: 510px; height: 290px; overflow: hidden;
  }
  .card--front {
    background: var(--card-dark);
    display: flex; align-items: center; justify-content: center; gap: 12px;
  }
  .brand-square {
    width: 22px; height: 22px; background: var(--orange);
  }
  .brand-name {
    color: var(--blue); font-weight: 600; font-size: 52px; letter-spacing: -0.5px;
  }
  .card--back { background: var(--card-light); }
  .contact {
    position: absolute; left: 36px; top: 40px; color: var(--ink);
  }
  .contact__name { color: var(--navy); font-size: 21px; font-weight: 600; line-height: 1.1; }
  .contact__role { font-size: 12px; margin-bottom: 12px; }
  .contact__lines { list-style: none; font-size: 13px; line-height: 17px; }
  .contact__lines li { display: flex; align-items: center; gap: 7px; }
  .icon { width: 11px; height: 11px; flex: none; }
  .address { margin-top: 12px; font-size: 13px; line-height: 16px; }
  .back-brand {
    position: absolute; right: 36px; top: 104px;
    display: flex; align-items: center; gap: 10px;
  }
  .back-brand .brand-name { font-size: 40px; }
  .back-brand .brand-square { width: 18px; height: 18px; }
  .base-band {
    position: absolute; left: 0; right: 0; bottom: 0; height: 22px;
    background: linear-gradient(90deg, var(--navy) 0 32%, var(--blue) 32% 100%);
  }
</style>
</head>
<body>
<main class="canvas">
  <section class="card card--front" aria-label="Card front">
    <span class="brand-square"></span>
    <span class="brand-name">MediqBay</span>
  </section>

  <section class="card card--back" aria-label="Card back">
    <div class="contact">
      <p class="contact__name">Paul Dwyer</p>
      <p class="contact__role">Director</p>
      <ul class="contact__lines">
        <li>
          <svg class="icon" viewBox="0 0 12 12"><rect width="12" height="12" rx="2" fill="var(--orange)"/><path d="M3 4.5h6M4 4.5v4h4v-4" stroke="#fff" stroke-width="1.3" fill="none"/></svg>
          03 9472 5836
        </li>
        <li>
          <svg class="icon" viewBox="0 0 12 12"><rect width="12" height="12" rx="2" fill="var(--orange)"/><rect x="4" y="2" width="4" height="8" rx="0.8" fill="none" stroke="#fff" stroke-width="1.2"/></svg>
          0438 275 904
        </li>
        <li>
          <svg class="icon" viewBox="0 0 12 12"><rect width="12" height="12" rx="2" fill="var(--orange)"/><path d="M2.5 3.5h7v5h-7zM2.5 3.5l3.5 3 3.5-3" stroke="#fff" stroke-width="1.1" fill="none"/></svg>
          firstname.lastname@mediqbay.com.au
        </li>
      </ul>
      <p class="address">
        Suite 31, 286 Keldon Street<br>
        Port Melbourne, Victoria<br>
        Fax: 03 8241 3975<br>
        mediqbay.com.au
      </p>
    </div>
    <div class="back-brand">
      <span class="brand-square"></span>
      <span class="brand-name">MediqBay</span>
    </div>
    <div class="base-band"></div>
  </section>
</main>
</body>
</html>
```